Figma App design and working prototype

I need to create a User Interface design and a Working prototype using Figma or similar. I’d also like all the assets and guidelines needed to guide the App developers to create the final product.
So, I'll need Design files and assets but you that I can give to an App development company or a freelance developer to create Android and iOS apps.

This app is an app for adults who wan to meet and have sex no strings attached.

The App name will be Nuvora

I have attached an app some pictures and a pdf file explaining details of the apps functions.

This app will be a sexy version of the pobalo app with a personals section used for adult services. I have attached images and a pdf below that will tell you the functions of the app.

I need an app interface design done for an app idea I have. I am nee to this it is my first time trying to launch an app and I do not know what you need in order to get what I need. I need a site map/ design and if possible a working prototype that I can pass on to an app developer that can deliver the final product. This model will be used to raise funds and give investors an idea of what the apps functions will do as detailed in the project brief. Any advise would be greatly appreciated. Please let me know if you have any questions. Looking forward to working with you.

Target Market(s)

Adults men and women looking for some adult entertainment

Industry/Entity Type

Adult entertainment Strip clubs

Colors
E54698
E96AAD
F1A4CE
F9D9EA
FCEFF6
A7469A
B969AE
D3A5CF
EDDBEB
F8F0F9
6B429C
8869AF
B7A5CE
E3DAEB
F3F0F8

Requirements
Must have
• An 18+ confirmation,
Nice to have
• A sexy feel.

```html
<!DOCTYPE html>
<html lang="en">
<head>
<meta charset="utf-8">
<title>Nuvora – Prototype Flow</title>
<link href="https://fonts.googleapis.com/css2?family=Montserrat:wght@500;700&family=Inter:wght@400;600&display=swap" rel="stylesheet">
<style>
:root{
  --canvas:#e5e5e5;
  --figma-blue:#18a0fb;
  --wire:#9fd0f7;
  --screen:#211e2b;
  --field:#34303f;
  --brand:#9b1ad6;
  --brand-soft:#b969ae;
  --muted:#8d879a;
  --ink:#111111;
  --white:#ffffff;
}
*{box-sizing:border-box;margin:0;padding:0}
html,body{width:1200px;height:900px;overflow:hidden}
body{background:var(--canvas);position:relative;font-family:"Inter",sans-serif}
.frame-label{position:absolute;top:159px;font-size:11px;color:var(--figma-blue);white-space:nowrap}
.flow-badge{position:absolute;left:15px;top:177px;width:68px;height:23px;background:var(--figma-blue);color:var(--white);font-size:11px;display:flex;align-items:center;gap:8px;padding-left:7px}
.flow-badge svg{width:10px;height:11px}
.selection{position:absolute;left:87px;top:177px;width:1064px;height:311px;border:1px solid var(--figma-blue)}
.handle{position:absolute;width:7px;height:7px;background:var(--white);border:1px solid var(--figma-blue)}
.size-tag{position:absolute;left:582px;top:497px;width:75px;height:18px;background:var(--figma-blue);color:var(--white);font-size:10px;font-weight:600;display:flex;align-items:center;justify-content:center;border-radius:2px}
.grip{position:absolute;left:1122px;top:458px;width:26px;height:26px;background:var(--figma-blue);border-radius:4px;display:flex;align-items:center;justify-content:center}
.screen{position:absolute;top:177px;width:88px;height:193px;background:var(--screen);outline:1px solid var(--figma-blue);overflow:hidden;font-size:4px;color:var(--muted)}
.screen.tall{height:311px}
.logo{color:var(--brand-soft);font-family:"Montserrat",sans-serif;font-weight:700;font-size:8px;text-align:center}
.field{height:9px;margin:4px 8px;background:var(--field);border-radius:2px;padding-left:3px;line-height:9px}
.btn{height:9px;margin:5px 8px;background:var(--brand);border-radius:2px;color:var(--white);text-align:center;line-height:9px}
.photo{background:linear-gradient(150deg,#c9987f,#6b3f3a 70%,#2d2230)}
.photo.dark{background:linear-gradient(160deg,#8a6a62,#3a2a36)}
.menu-head{height:22px;background:var(--brand);color:var(--white);font-family:"Montserrat",sans-serif;font-weight:700;font-size:7px;text-align:center;line-height:22px}
.menu-item{padding:5px 10px}
.grid{display:grid;grid-template-columns:1fr 1fr;gap:3px;padding:4px}
.grid .photo{height:44px;border-radius:2px}
.icons{display:grid;grid-template-columns:repeat(5,1fr);gap:3px;padding:6px 4px 0}
.icons span{height:11px;background:var(--brand);border-radius:2px}
.detail-row{display:flex;justify-content:space-between;padding:2px 8px;border-bottom:1px solid #2d2a38}
.bottom-bar{position:absolute;left:0;right:0;bottom:0;height:14px;background:#1a1823;display:flex;justify-content:space-around;align-items:center}
.bottom-bar span{width:6px;height:6px;background:var(--brand);border-radius:50%}
.pill{position:absolute;bottom:22px;left:30px;width:26px;height:10px;background:var(--brand);border-radius:5px}
.modal{margin:22px 6px;background:#2b2836;border-radius:3px;padding:6px}
.check{display:flex;align-items:center;gap:3px;padding:3px 0}
.check i{width:4px;height:4px;border:1px solid var(--muted)}
.headline{position:absolute;left:172px;top:562px;font-family:"Montserrat",sans-serif;font-weight:700;font-size:51px;line-height:70px;color:var(--ink)}
.wires{position:absolute;left:0;top:0;pointer-events:none}
</style>
</head>
<body>

<div class="flow-badge">Flow 1
  <svg viewBox="0 0 10 11"><path d="M1 1 L9 5.5 L1 10 Z" fill="none" stroke="#fff" stroke-width="1.3"/></svg>
</div>

<span class="frame-label" style="left:87px">Login</span>
<span class="frame-label" style="left:195px">Sign Up</span>
<span class="frame-label" style="left:305px">Home Sidem...</span>
<span class="frame-label" style="left:414px">Home</span>
<span class="frame-label" style="left:524px">Escort Detail...</span>
<span class="frame-label" style="left:632px">Escort Detail...</span>
<span class="frame-label" style="left:741px">Post Ad Tak...</span>
<span class="frame-label" style="left:849px">Post Ad Tak...</span>
<span class="frame-label" style="left:959px">Post Ad Det...</span>
<span class="frame-label" style="left:1064px">Post Ad Det...</span>

<!-- Login -->
<section class="screen" style="left:87px">
  <p class="logo" style="margin-top:48px;margin-bottom:12px">Nuvora</p>
  <div class="field">Username</div>
  <div class="field">Password</div>
  <div class="btn" style="margin-top:14px">Login</div>
  <p style="text-align:center">Forgot password? Sign up</p>
</section>

<!-- Sign Up -->
<section class="screen" style="left:195px">
  <p class="logo" style="margin-top:48px;margin-bottom:8px">Nuvora</p>
  <div class="field">Name</div>
  <div class="field">Email</div>
  <div class="field">Password</div>
  <div class="btn" style="margin-top:18px">Sign Up</div>
</section>

<!-- Home Sidemenu -->
<section class="screen" style="left:305px">
  <div class="menu-head">Nuvora</div>
  <p style="color:var(--brand-soft);text-align:center;padding:6px 0">Welcome</p>
  <p class="menu-item">Home</p>
  <p class="menu-item">My Ads</p>
  <p class="menu-item">Chats</p>
  <p class="menu-item">Favourites</p>
  <p class="menu-item">Logout</p>
</section>

<!-- Home -->
<section class="screen tall" style="left:414px">
  <div class="field" style="margin:6px 4px 0"></div>
  <div class="icons"><span></span><span></span><span></span><span></span><span></span><span></span><span></span><span></span><span></span><span></span></div>
  <div class="grid">
    <div class="photo" role="img" aria-label="Profile photo"></div>
    <div class="photo dark" role="img" aria-label="Profile photo"></div>
    <div class="photo dark" role="img" aria-label="Profile photo"></div>
    <div class="photo" role="img" aria-label="Profile photo"></div>
    <div class="photo" role="img" aria-label="Profile photo"></div>
    <div class="photo dark" role="img" aria-label="Profile photo"></div>
    <div class="photo dark" role="img" aria-label="Profile photo"></div>
    <div class="photo" role="img" aria-label="Profile photo"></div>
    <div class="photo" role="img" aria-label="Profile photo"></div>
    <div class="photo dark" role="img" aria-label="Profile photo"></div>
  </div>
  <div class="bottom-bar"><span></span><span></span><span></span><span></span></div>
</section>

<!-- Escort Detail 1 & 2 -->
<section class="screen tall" style="left:524px">
  <div class="photo" style="height:62px" role="img" aria-label="Profile cover photo"></div>
  <div style="height:40px"></div>
  <div class="detail-row"><span>Age</span><span>24</span></div>
  <div class="detail-row"><span>Height</span><span>5'6</span></div>
  <div class="detail-row"><span>Hair</span><span>Blonde</span></div>
  <div class="detail-row"><span>Eyes</span><span>Blue</span></div>
  <div class="detail-row"><span>City</span><span>Toronto</span></div>
  <div class="detail-row"><span>Rates</span><span>$200</span></div>
  <div class="bottom-bar" style="background:var(--brand)"></div>
</section>
<section class="screen tall" style="left:632px">
  <div class="photo" style="height:62px" role="img" aria-label="Profile cover photo"></div>
  <div style="height:40px"></div>
  <div class="detail-row"><span>Age</span><span>24</span></div>
  <div class="detail-row"><span>Height</span><span>5'6</span></div>
  <div class="detail-row"><span>Hair</span><span>Blonde</span></div>
  <div class="detail-row"><span>Eyes</span><span>Blue</span></div>
  <div class="detail-row"><span>City</span><span>Toronto</span></div>
  <div class="detail-row"><span>Rates</span><span>$200</span></div>
  <div class="bottom-bar" style="background:var(--brand)"></div>
</section>

<!-- Post Ad Take Photo -->
<section class="screen" style="left:741px">
  <div class="photo" style="position:absolute;left:3px;right:3px;top:20px;height:130px" role="img" aria-label="Camera preview photo"></div>
  <span class="pill"></span>
</section>
<section class="screen" style="left:849px">
  <div class="photo dark" style="position:absolute;left:3px;right:3px;top:20px;height:130px" role="img" aria-label="Camera preview photo"></div>
  <span class="pill"></span>
</section>

<!-- Post Ad Details -->
<section class="screen" style="left:959px">
  <svg viewBox="0 0 20 16" style="display:block;width:16px;margin:14px auto 10px"><rect x="1" y="3" width="18" height="12" rx="2" fill="none" stroke="#8d879a"/><circle cx="10" cy="9" r="3.5" fill="none" stroke="#8d879a"/></svg>
  <div class="field">Title</div>
  <div class="field">Category</div>
  <div class="field">Price</div>
  <div class="btn" style="margin-left:44px">Post Ad</div>
  <div class="bottom-bar"><span></span><span></span><span></span><span></span></div>
</section>
<section class="screen" style="left:1064px">
  <div class="modal">
    <p style="color:var(--white);margin-bottom:3px">Categories</p>
    <div class="check"><i></i>Escort</div>
    <div class="check"><i></i>Massage</div>
    <div class="check"><i></i>Dating</div>
    <div class="check"><i></i>Cam</div>
  </div>
</section>

<svg class="wires" width="1200" height="900" viewBox="0 0 1200 900">
  <g fill="none" stroke="var(--wire)" stroke-width="1.6">
    <path d="M170 287 C300 287 330 330 414 330"/>
    <path d="M170 281 C230 260 260 230 305 225"/>
    <path d="M276 316 C330 330 380 335 414 335"/>
    <path d="M390 188 C440 200 460 300 496 330"/>
    <path d="M496 330 C520 300 540 210 600 188"/>
    <path d="M496 330 C560 250 600 220 680 188"/>
    <path d="M496 330 C600 260 700 200 750 188"/>
    <path d="M496 330 C620 230 780 200 860 188"/>
    <path d="M496 330 C640 220 880 190 960 188"/>
    <path d="M496 330 C620 240 980 180 1075 188"/>
    <path d="M599 290 C640 300 680 310 720 300"/>
    <path d="M680 290 C740 340 760 360 810 355"/>
    <path d="M560 475 C650 470 760 420 815 356"/>
    <path d="M815 356 C850 330 880 300 900 280"/>
    <path d="M900 188 C930 230 940 260 960 275"/>
    <path d="M935 275 C980 270 1000 260 1040 270"/>
    <path d="M1040 188 C1060 250 1080 270 1151 277"/>
  </g>
  <g fill="#ffffff">
    <circle cx="170" cy="287" r="5"/><circle cx="276" cy="316" r="5"/><circle cx="390" cy="188" r="5"/>
    <circle cx="496" cy="330" r="5"/><circle cx="600" cy="188" r="5"/><circle cx="680" cy="188" r="5"/>
    <circle cx="750" cy="188" r="5"/><circle cx="860" cy="188" r="5"/><circle cx="960" cy="188" r="5"/>
    <circle cx="1075" cy="188" r="5"/><circle cx="599" cy="290" r="5"/><circle cx="680" cy="290" r="5"/>
    <circle cx="815" cy="356" r="5"/><circle cx="900" cy="188" r="5"/><circle cx="935" cy="275" r="5"/>
    <circle cx="1040" cy="188" r="5"/><circle cx="1151" cy="277" r="5"/><circle cx="560" cy="475" r="5"/>
  </g>
</svg>

<div class="selection"></div>
<span class="handle" style="left:84px;top:174px"></span>
<span class="handle" style="left:1148px;top:174px"></span>
<span class="handle" style="left:84px;top:485px"></span>
<span class="handle" style="left:1148px;top:485px"></span>
<div class="size-tag">4367 × 1282</div>
<div class="grip">
  <svg width="12" height="12" viewBox="0 0 12 12"><g stroke="#fff" stroke-width="1.5"><path d="M3 2v8M6 2v8M9 2v8"/></g></svg>
</div>

<h1 class="headline">The prototype is not complete.<br>I have messaged you the<br>prototype link</h1>

</body>
</html>
```